An A5, double sided, ticklist

This is for a game at our Pilates + Yoga Studio. A list of things that they need to tick off over the month to earn different points. There are different point categories - a 1 point, 2 point, 5 point and 10 point category.

Under each category is a task they have to complete. ie Under 1 point is: * attend a reformer class * attend a yoga class * attend a sculpt class * follow the studio on Pictora

Under 2 points is
* do two classes in a row * do a class with a teacher you haven't had in the last month * write a review for your class on Zestaloop

Under 3 points is:
* bring a friend or family member to class (not a current member) *wear a piece of studio merch to class * write a Brindle review

Under 5 points is:
* wear a costume to class and keep it on for the class * have a friend/family member register at the studio as a member this month

Beside each line of a task to complete can there by 3 tick boxes please (ie they can achieve each task 3 times). And then at the end of those tick boxes is space for a total (ie 3 x 2 points = 6).

At the end of each section is their total number of points for that section, and then at the end of the card is the grand total.

It is REQUIRED that this design is made in Canva so that I have access to the design once it's completed so I can add in extra category lines as I think of them.

The caption for the card is Maple Ember Studio Birthday 2026!

Colours to use are yellow, white + orange. You can see our website here - mapleemberstudio.nz or our Pictora @maple_emberstudio to get a feel for the studio + the colours we use!

Thank you!

```html
<!DOCTYPE html>
<html lang="en">
<head>
<meta charset="utf-8">
<title>Maple Ember Studio Birthday 2026 ticklist</title>
<link href="https://fonts.googleapis.com/css2?family=Abril+Fatface&family=Barlow:wght@400;500;700&family=Damion&family=Montserrat:wght@500&display=swap" rel="stylesheet">
<style>
  :root{
    --backdrop:#8c8c8c;
    --cream:#fbeed6;
    --beige:#e7d8c1;
    --orange:#fb8a2e;
    --orange-deep:#f37a1f;
    --orange-dark:#d9651a;
    --yellow:#f9b54a;
    --yellow-bright:#fbbd3c;
    --ring:#e3a286;
    --ink:#3b3431;
    --white:#ffffff;
    --box-line:#f3cf9a;
    --rule:#b9a89a;
  }
  *{box-sizing:border-box;margin:0;padding:0}
  html,body{width:1200px;height:851px;overflow:hidden}
  body{background:var(--backdrop);position:relative;font-family:"Barlow",sans-serif;color:var(--ink)}

  .page{position:absolute;top:50px;width:526px;height:747px;background:var(--cream);overflow:hidden;box-shadow:0 2px 6px rgba(0,0,0,.25)}
  .page--front{left:44px}
  .page--back{left:602px}
  .page-shapes{position:absolute;inset:0;width:100%;height:100%}
  .art{position:absolute;border-radius:40%}

  .studio-name{position:absolute;font-family:"Barlow",sans-serif;font-weight:700;color:var(--yellow);text-align:center;text-transform:uppercase;letter-spacing:1px;line-height:1.05}

  /* front */
  .front-title{position:absolute;left:0;width:100%;text-align:center;font-weight:400}
  .front-title__script{font-family:"Damion",cursive;color:var(--orange);font-size:62px;top:218px}
  .front-title__serif{font-family:"Abril Fatface",serif;color:var(--yellow-bright);font-size:64px;line-height:1}
  .front-title__serif--one{top:288px}
  .front-title__serif--two{top:355px}
  .ribbon{position:absolute;left:46px;top:427px;width:434px;height:74px}
  .ribbon__label{position:absolute;left:110px;top:427px;width:306px;height:63px;display:flex;align-items:center;justify-content:center;font-family:"Montserrat",sans-serif;font-weight:500;color:var(--white);font-size:46px;letter-spacing:1px}
  .front-year{position:absolute;left:0;width:100%;top:494px;text-align:center;font-family:"Abril Fatface",serif;color:var(--orange-deep);font-size:66px}

  /* back */
  .back-heading{position:absolute;left:50px;top:98px;display:flex;align-items:baseline;gap:10px;font-weight:400}
  .back-heading__script{font-family:"Damion",cursive;color:var(--orange-deep);font-size:76px;line-height:1}
  .back-heading__year{font-family:"Abril Fatface",serif;color:var(--yellow);font-size:50px;line-height:1}

  .section{position:absolute;left:63px;width:408px;height:99px;border:1px solid var(--yellow);border-radius:12px;background:rgba(251,238,214,.85)}
  .section__badge{position:absolute;left:-27px;top:50%;width:50px;height:50px;margin-top:-25px;border-radius:50%;display:flex;flex-direction:column;align-items:center;justify-content:center;color:var(--white);line-height:1}
  .section__badge b{font-size:20px;font-weight:700}
  .section__badge span{font-size:9px;letter-spacing:.3px}
  .section__badge--orange{background:var(--orange)}
  .section__badge--yellow{background:var(--yellow)}
  .tasks{list-style:none;padding:6px 0 0 32px}
  .tasks--low{padding-top:12px}
  .task{display:flex;align-items:flex-start;min-height:12px;margin-bottom:5px;font-size:10px;line-height:1.2}
  .task__text{width:222px;padding-left:10px;padding-right:8px;position:relative}
  .task__text::before{content:"";position:absolute;left:0;top:3px;width:5px;height:5px;border-radius:50%;background:var(--orange)}
  .task__boxes{display:flex;gap:7px}
  .tick{width:14px;height:12px;border:1px solid var(--box-line);background:var(--white)}
  .task__equals{margin-left:9px;width:10px;font-size:10px}
  .task__line{width:70px;height:10px;border-bottom:1px solid var(--rule)}
  .section__total{position:absolute;left:31px;bottom:6px;width:111px;height:15px;border-radius:3px;color:var(--white);font-size:10px;font-weight:700;letter-spacing:.4px;display:flex;align-items:center;justify-content:center}
  .section__total--orange{background:var(--orange)}
  .section__total--yellow{background:var(--yellow)}
  .section__field{position:absolute;left:254px;bottom:5px;width:142px;height:18px;border:1px solid #f6dcb4;border-radius:4px;background:var(--white)}

  .grand-total{position:absolute;left:67px;top:633px;width:398px;height:44px;border:1px solid var(--yellow);border-radius:10px;background:var(--cream);display:flex;align-items:center;padding-left:38px}
  .grand-total__label{font-weight:700;color:var(--orange-dark);font-size:23px;letter-spacing:.5px}
  .grand-total__field{position:absolute;left:220px;top:8px;width:138px;height:27px;border:1px solid var(--yellow);border-radius:4px;background:var(--white)}
  .web-address{position:absolute;left:0;width:100%;top:699px;text-align:center;font-weight:700;font-size:13px;letter-spacing:2.4px;color:var(--yellow)}
</style>
</head>
<body>

<section class="page page--front">
  <svg class="page-shapes" viewBox="0 0 526 747" aria-hidden="true">
    <path d="M0 0H226C214 40 175 60 140 90C100 125 60 160 45 220C35 250 20 265 0 275Z" fill="var(--orange)"/>
    <path d="M358 0H526V155C500 160 480 150 460 155C420 165 400 160 392 130C385 90 370 70 360 40Z" fill="var(--yellow)"/>
    <path d="M0 490C60 470 110 500 160 540C220 585 300 640 400 615C460 600 500 560 526 540V747H0Z" fill="var(--beige)"/>
    <ellipse cx="96" cy="97" rx="64" ry="60" fill="none" stroke="var(--ring)" stroke-width="4"/>
  </svg>
  <div class="art" role="img" aria-label="Scattered dot pattern in soft peach" style="left:325px;top:10px;width:143px;height:120px;background:rgba(232,160,110,.18)"></div>
  <div class="art" role="img" aria-label="Line drawing of a seated figure in meditation" style="left:396px;top:130px;width:130px;height:151px;background:rgba(59,80,72,.08)"></div>
  <div class="art" role="img" aria-label="Scattered dot pattern in soft peach" style="left:4px;top:281px;width:88px;height:105px;background:rgba(232,160,110,.18)"></div>
  <div class="art" role="img" aria-label="Line drawing of palm leaves in teal" style="left:0;top:562px;width:150px;height:167px;background:rgba(91,133,128,.15)"></div>
  <div class="art" role="img" aria-label="Line drawing of a monstera leaf in soft pink" style="left:352px;top:562px;width:126px;height:180px;background:rgba(227,162,134,.18)"></div>

  <div class="studio-name" style="left:186px;top:140px;width:172px;font-size:20px">Maple Ember<br>Studio</div>

  <h1>
    <span class="front-title front-title__script">Maple</span>
    <span class="front-title front-title__serif front-title__serif--one">Ember</span>
    <span class="front-title front-title__serif front-title__serif--two">Studio</span>
  </h1>

  <svg class="ribbon" viewBox="0 0 434 74" aria-hidden="true">
    <polygon points="0,10 90,10 90,74 0,74 22,42" fill="var(--orange)"/>
    <polygon points="344,10 434,10 412,42 434,74 344,74" fill="var(--orange)"/>
    <polygon points="64,63 90,74 90,63" fill="var(--orange-dark)"/>
    <polygon points="370,63 344,74 344,63" fill="var(--orange-dark)"/>
    <rect x="64" y="0" width="306" height="63" fill="var(--orange-deep)"/>
  </svg>
  <div class="ribbon__label">BIRTHDAY</div>
  <div class="front-year">2026</div>
</section>

<section class="page page--back">
  <svg class="page-shapes" viewBox="0 0 526 747" aria-hidden="true">
    <path d="M0 0H80C60 30 40 50 30 90C22 125 15 160 0 175Z" fill="var(--orange)"/>
    <path d="M20 30C45 15 70 10 90 0H110C80 20 55 45 45 80C38 110 25 150 8 175L0 175V70Z" fill="#fba05a" opacity=".8"/>
    <path d="M365 0H526V160C505 175 485 160 470 150C440 130 420 130 405 110C390 85 385 45 365 0Z" fill="var(--yellow)"/>
    <path d="M0 565C50 560 80 600 120 630C170 665 250 690 330 665C400 645 440 600 480 580C500 570 515 570 526 572V747H0Z" fill="var(--beige)"/>
    <path d="M526 600C500 610 480 640 478 680C476 710 460 730 430 747H526Z" fill="var(--yellow)"/>
  </svg>
  <div class="art" role="img" aria-label="Sprig of leaves in soft yellow" style="left:60px;top:0;width:93px;height:75px;background:rgba(249,181,74,.3)"></div>
  <div class="art" role="img" aria-label="Scattered dot pattern in soft peach" style="left:328px;top:8px;width:142px;height:126px;background:rgba(232,160,110,.18)"></div>
  <div class="art" role="img" aria-label="Small yellow leaf sprig" style="left:0;top:382px;width:44px;height:55px;background:rgba(249,181,74,.35)"></div>
  <div class="art" role="img" aria-label="Small yellow leaf sprig" style="left:496px;top:528px;width:30px;height:30px;background:rgba(249,181,74,.35)"></div>
  <div class="art" role="img" aria-label="Line drawing of palm leaves in teal" style="left:0;top:604px;width:86px;height:142px;background:rgba(91,133,128,.15)"></div>
  <div class="art" role="img" aria-label="Scattered dot pattern in soft peach" style="left:430px;top:688px;width:76px;height:58px;background:rgba(232,160,110,.25)"></div>

  <div class="studio-name" style="left:188px;top:52px;width:104px;font-size:14px;color:var(--orange)">Maple Ember<br>Studio</div>

  <h2 class="back-heading">
    <span class="back-heading__script">Birthday</span>
    <span class="back-heading__year">2026</span>
  </h2>

  <div class="section" style="top:189px">
    <div class="section__badge section__badge--orange"><b>01</b><span>POINT</span></div>
    <ul class="tasks">
      <li class="task"><span class="task__text">Attend a reformer class</span><span class="task__boxes"><i class="tick"></i><i class="tick"></i><i class="tick"></i></span><span class="task__equals">=</span><span class="task__line"></span></li>
      <li class="task"><span class="task__text">Attend a yoga class</span><span class="task__boxes"><i class="tick"></i><i class="tick"></i><i class="tick"></i></span><span class="task__equals">=</span><span class="task__line"></span></li>
      <li class="task"><span class="task__text">Attend a sculpt class</span><span class="task__boxes"><i class="tick"></i><i class="tick"></i><i class="tick"></i></span><span class="task__equals">=</span><span class="task__line"></span></li>
      <li class="task"><span class="task__text">Follow the studio on Pictora</span><span class="task__boxes"><i class="tick"></i><i class="tick"></i><i class="tick"></i></span><span class="task__equals">=</span><span class="task__line"></span></li>
    </ul>
    <div class="section__total section__total--orange">SECTION TOTAL</div>
    <div class="section__field"></div>
  </div>

  <div class="section" style="top:300px">
    <div class="section__badge section__badge--yellow"><b>02</b><span>POINT</span></div>
    <ul class="tasks">
      <li class="task"><span class="task__text">Do two classes in a row</span><span class="task__boxes"><i class="tick"></i><i class="tick"></i><i class="tick"></i></span><span class="task__equals">=</span><span class="task__line"></span></li>
      <li class="task"><span class="task__text">Do a class with a teacher you haven't had in the last month</span><span class="task__boxes"><i class="tick"></i><i class="tick"></i><i class="tick"></i></span><span class="task__equals">=</span><span class="task__line"></span></li>
      <li class="task"><span class="task__text">Write a review for your class on Zestaloop</span><span class="task__boxes"><i class="tick"></i><i class="tick"></i><i class="tick"></i></span><span class="task__equals">=</span><span class="task__line"></span></li>
    </ul>
    <div class="section__total section__total--yellow">SECTION TOTAL</div>
    <div class="section__field"></div>
  </div>

  <div class="section" style="top:410px">
    <div class="section__badge section__badge--orange"><b>03</b><span>POINT</span></div>
    <ul class="tasks">
      <li class="task"><span class="task__text">Bring a friend or family member to class (not a current member)</span><span class="task__boxes"><i class="tick"></i><i class="tick"></i><i class="tick"></i></span><span class="task__equals">=</span><span class="task__line"></span></li>
      <li class="task"><span class="task__text">Wear a piece of studio merch to class</span><span class="task__boxes"><i class="tick"></i><i class="tick"></i><i class="tick"></i></span><span class="task__equals">=</span><span class="task__line"></span></li>
      <li class="task"><span class="task__text">Write a Brindle review</span><span class="task__boxes"><i class="tick"></i><i class="tick"></i><i class="tick"></i></span><span class="task__equals">=</span><span class="task__line"></span></li>
    </ul>
    <div class="section__total section__total--orange">SECTION TOTAL</div>
    <div class="section__field"></div>
  </div>

  <div class="section" style="top:523px">
    <div class="section__badge section__badge--yellow"><b>05</b><span>POINT</span></div>
    <ul class="tasks tasks--low">
      <li class="task"><span class="task__text">wear a costume to class and keep it on for the class</span><span class="task__boxes"><i class="tick"></i><i class="tick"></i><i class="tick"></i></span><span class="task__equals">=</span><span class="task__line"></span></li>
      <li class="task"><span class="task__text">have a friend/family member register at the studio as a member this month</span><span class="task__boxes"><i class="tick"></i><i class="tick"></i><i class="tick"></i></span><span class="task__equals">=</span><span class="task__line"></span></li>
    </ul>
    <div class="section__total section__total--yellow">SECTION TOTAL</div>
    <div class="section__field"></div>
  </div>

  <div class="grand-total">
    <span class="grand-total__label">GRAND TOTAL</span>
    <span class="grand-total__field"></span>
  </div>

  <p class="web-address">www.mapleemberstudio.nz</p>
</section>

</body>
</html>
```